Rollup Banner & Flyer für eine Messe "Erfolg durch Innovation"

Wir benötigten für eine Messe einen Roll Up Banner und Flyer zum verteilen. Gerne basierend auf der aktuellen Firmenpräsentation und mit unseren Referenzen.
Im flyer sollen unserer Leistungen (Datenanalyse, Simulation, Optimierung und Webapplikation) dargestellt werden mit einem kleinen Text und einem aussagekräftigen bild. (https://www.kalvento.ch/leistungen/)

Target Market(s)

Industrie

Industry/Entity Type

Simulation

Font styles to use
Sans Serif
Other font styles liked:
• Roboto

Requirements
Must have
• Logo, Referenzen

```html
<!DOCTYPE html>
<html lang="de">
<head>
<meta charset="utf-8">
<title>Kalvento – Flyer</title>
<link href="https://fonts.googleapis.com/css2?family=Poppins:wght@400;500;700;800&display=swap" rel="stylesheet">
<style>
  :root {
    --black: #000000;
    --lime: #dde064;
    --lime-light: #eef0c2;
    --lime-pale: #f4f5d8;
    --grey-dark: #232323;
    --grey-mid: #5a5a5a;
    --white: #ffffff;
    --stage: #ececec;
  }
  * { box-sizing: border-box; margin: 0; padding: 0; }
  html, body {
    width: 1200px; height: 2182px; overflow: hidden;
    background: var(--stage);
    font-family: "Poppins", sans-serif;
  }
  .flyer {
    position: absolute; left: 0; top: 236px;
    width: 1200px; height: 1710px;
    background: var(--lime-light);
    overflow: hidden;
  }
  .hero-shapes { position: absolute; left: 0; top: 0; width: 1200px; height: 742px; }
  .brand {
    position: absolute; left: 50px; top: 120px;
    display: flex; align-items: center; gap: 22px; color: var(--white);
  }
  .brand-mark {
    width: 96px; height: 96px; border-radius: 50%;
    border: 8px solid var(--white);
  }
  .brand-name { font-weight: 700; font-size: 74px; line-height: 1; letter-spacing: 2px; }
  .brand-tag { font-weight: 500; font-size: 25px; letter-spacing: 2px; margin-top: 4px; }
  .monitor {
    position: absolute; left: 715px; top: 352px; width: 452px; height: 466px;
    background: linear-gradient(180deg, #f2f2f2 0%, #cfcfcf 100%);
    border-radius: 12px; z-index: 2;
  }
  .headline {
    position: absolute; left: 52px; top: 590px;
    font-weight: 800; font-size: 48px; line-height: 60px; color: var(--black);
  }
  .strap {
    position: absolute; left: 0; top: 742px; width: 1200px; height: 151px;
    background: linear-gradient(180deg, var(--grey-mid) 0%, var(--grey-dark) 100%);
    padding: 26px 52px 0;
  }
  .strap-title { color: var(--lime); font-weight: 800; font-size: 34px; line-height: 46px; }
  .strap-sub { color: var(--white); font-weight: 700; font-size: 32px; line-height: 48px; }
  .services {
    position: absolute; left: 0; top: 893px; width: 1200px; height: 749px;
    display: grid; grid-template-columns: 1fr 1fr; grid-template-rows: 1fr 1fr;
    gap: 5px; background: var(--white); padding: 5px;
  }
  .service { padding: 32px 30px 0 30px; }
  .service--dark { background: var(--black); color: var(--white); }
  .service--dark .service-title { color: var(--lime); }
  .service--light { background: var(--lime); color: var(--black); }
  .service-head { display: flex; align-items: center; gap: 20px; margin-bottom: 26px; }
  .service-icon { width: 60px; height: 60px; flex: none; }
  .service-title { font-weight: 700; font-size: 48px; line-height: 60px; }
  .service-text { font-size: 23px; line-height: 32px; font-weight: 400; }
  .footer {
    position: absolute; left: 0; top: 1647px; width: 1200px; height: 63px;
    display: grid; grid-template-columns: 1fr 1fr; gap: 5px; background: var(--white);
    font-weight: 700; font-size: 20px;
  }
  .footer-call { background: var(--grey-dark); color: var(--lime); display: flex; align-items: center; justify-content: center; }
  .footer-web { background: var(--lime); color: var(--black); display: flex; align-items: center; justify-content: center; }
</style>
</head>
<body>
<main class="flyer">
  <svg class="hero-shapes" viewBox="0 0 1200 742" aria-hidden="true">
    <rect width="1200" height="742" fill="var(--lime-light)"/>
    <circle cx="980" cy="720" r="640" fill="var(--lime)"/>
    <path d="M0 0 H640 C610 330 380 520 0 530 Z" fill="var(--black)"/>
    <rect x="0" y="555" width="1200" height="187" fill="var(--lime)"/>
  </svg>

  <div class="brand">
    <span class="brand-mark"></span>
    <div>
      <div class="brand-name">KALVENTO</div>
      <div class="brand-tag">SIMULATION &amp; ANALYTICS</div>
    </div>
  </div>

  <h1 class="headline">IHR NÄCHSTER SCHRITT –<br>INTELLIGENTER GEMACHT.</h1>

  <div class="monitor" role="img" aria-label="Bildschirm mit einer Auswertung der Tourenplanung: Karte mit Routen, Tabelle und Balkendiagramme"></div>

  <section class="strap">
    <p class="strap-title">STRATEGISCHE ENTSCHEIDUNGEN</p>
    <p class="strap-sub">unterstützt durch Simulation, optimiert durch Analytik.</p>
  </section>

  <section class="services">
    <article class="service service--dark">
      <div class="service-head">
        <svg class="service-icon" viewBox="0 0 60 60" fill="none" stroke="currentColor" stroke-width="2.5">
          <ellipse cx="30" cy="30" rx="26" ry="11"/>
          <ellipse cx="30" cy="30" rx="26" ry="11" transform="rotate(60 30 30)"/>
          <ellipse cx="30" cy="22" rx="8" ry="3"/>
          <path d="M22 22 V38 C22 42 38 42 38 38 V22"/>
          <path d="M22 30 C22 34 38 34 38 30"/>
        </svg>
        <h2 class="service-title">Datenanalyse</h2>
      </div>
      <p class="service-text">Datenanalyse macht Prozesse sichtbar, erkennt Muster und schafft eine objektive Grundlage für Entscheidungen. Wir strukturieren, bereinigen und analysieren Daten so, dass sie einen echten Nutzen erzeugen.</p>
    </article>

    <article class="service service--light">
      <div class="service-head">
        <svg class="service-icon" viewBox="0 0 60 60" fill="none" stroke="currentColor" stroke-width="2.5">
          <rect x="4" y="10" width="52" height="38" rx="2"/>
          <path d="M8 24 H16 L20 16 L25 30 L29 22 H36"/>
          <rect x="40" y="15" width="11" height="11"/>
          <rect x="9" y="34" width="10" height="9"/>
          <rect x="24" y="34" width="10" height="9"/>
          <circle cx="45" cy="38" r="4"/>
          <path d="M2 52 H58"/>
        </svg>
        <h2 class="service-title">Simulation</h2>
      </div>
      <p class="service-text">Simulation bildet reale Prozesse digital ab, damit Abläufe, Kapazitäten und Varianten risikofrei getestet werden können.</p>
    </article>

    <article class="service service--light">
      <div class="service-head">
        <svg class="service-icon" viewBox="0 0 60 60" fill="none" stroke="currentColor" stroke-width="2.5">
          <rect x="18" y="4" width="24" height="26" rx="2"/>
          <path d="M23 12 H37 M23 18 H37 M23 24 H32"/>
          <circle cx="30" cy="44" r="8"/>
          <circle cx="30" cy="44" r="3"/>
          <path d="M30 30 V36 M8 20 V52 M52 20 V52 M4 36 H12 M48 36 H56"/>
        </svg>
        <h2 class="service-title">Optimierung</h2>
      </div>
      <p class="service-text">Optimierung sucht automatisch nach der besten Lösung – sei es bei Planung, Ressourcen, Routen oder Abläufen. Mit Algorithmen und intelligenten Modellen finden wir Varianten, die Kosten senken, Kapazitäten besser nutzen und Entscheidungen beschleunigen.</p>
    </article>

    <article class="service service--dark">
      <div class="service-head">
        <svg class="service-icon" viewBox="0 0 60 60" fill="none" stroke="currentColor" stroke-width="2.5">
          <rect x="4" y="8" width="52" height="36" rx="2"/>
          <path d="M4 16 H56"/>
          <rect x="12" y="22" width="18" height="12"/>
          <path d="M36 24 H48 M36 30 H46"/>
          <path d="M24 44 L22 52 H38 L36 44"/>
        </svg>
        <h2 class="service-title">Webapplikationen</h2>
      </div>
      <p class="service-text">Wir entwickeln individuelle Webapplikationen, die Daten, Simulationen und Optimierungen in einem benutzerfreundlichen Tool usammenführen. So entstehen Lösungen, die direkt im Alltag genutzt werden – einfach, schnell und ohne Installation.</p>
    </article>
  </section>

  <footer class="footer">
    <div class="footer-call">CALL US: +41 81 555 0147</div>
    <div class="footer-web">INFO@KALVENTO.CH | WWW.KALVENTO.CH</div>
  </footer>
</main>
</body>
</html>
```